Realty Group Needs Classy, Contemporary Letterhead Design

We need a letterhead design for a new realty company located in NY, USA. We buy investment properties to rehabilitate and or keep in our rental portfolio.

```html
<!DOCTYPE html>
<html lang="en">
<head>
<meta charset="utf-8">
<title>Halvorsen Realty Group Letterhead</title>
<link href="https://fonts.googleapis.com/css2?family=Open+Sans:wght@400;600;800&display=swap" rel="stylesheet">
<style>
  :root {
    --backdrop: #d9d9d9;
    --paper: #f7f7f7;
    --brand-purple: #4b2a7f;
    --footer-grey: #555555;
    --body-text: #4a4a4a;
    --muted: #8a8a8a;
    --footer-text: #f2f2f2;
  }
  * { margin: 0; padding: 0; box-sizing: border-box; }
  html, body {
    width: 1200px;
    height: 686px;
    overflow: hidden;
    background: var(--backdrop);
    font-family: "Open Sans", Arial, sans-serif;
  }
  .letterhead {
    position: absolute;
    left: 370px;
    top: 18px;
    width: 460px;
    height: 650px;
    background: var(--paper);
    box-shadow: 0 4px 14px rgba(0,0,0,0.18);
    overflow: hidden;
  }
  .brand {
    position: absolute;
    top: 52px;
    left: 0;
    width: 100%;
    text-align: center;
  }
  .brand-name {
    font-weight: 800;
    font-size: 27px;
    letter-spacing: 0.5px;
    color: var(--brand-purple);
    line-height: 1;
  }
  .brand-tagline {
    margin-top: 3px;
    font-weight: 600;
    font-size: 8px;
    letter-spacing: 1px;
    color: var(--muted);
  }
  .letter-body {
    position: absolute;
    top: 138px;
    left: 46px;
    right: 42px;
    font-size: 9.6px;
    line-height: 1.42;
    color: var(--body-text);
  }
  .letter-body p + p { margin-top: 13px; }
  .signature {
    position: absolute;
    top: 436px;
    right: 58px;
    width: 78px;
    height: 40px;
    background: linear-gradient(90deg, rgba(75,42,127,0.06), rgba(75,42,127,0.14), rgba(75,42,127,0.06));
    border-radius: 4px;
  }
  .footer {
    position: absolute;
    left: 0;
    bottom: 0;
    width: 460px;
    height: 80px;
  }
  .footer-band { position: absolute; left: 0; top: 0; }
  .footer-label {
    position: absolute;
    height: 12px;
    font-size: 8.5px;
    line-height: 12px;
    color: var(--footer-text);
    display: flex;
    align-items: center;
    gap: 7px;
    white-space: nowrap;
  }
  .footer-label svg { width: 8px; height: 9px; flex: none; }
  .label-address { left: 22px; bottom: 8px; }
  .label-phone { left: 232px; bottom: 27px; }
  .label-email { left: 350px; bottom: 27px; }
</style>
</head>
<body>
  <main class="letterhead">
    <header class="brand">
      <div class="brand-name">HALVORSEN</div>
      <div class="brand-tagline">Realty Group, LLC</div>
    </header>

    <section class="letter-body">
      <p>There are many variations of passages of Lorem Ipsum available, but the majority have suffered alteration in some form, by injected humour, or randomised words which don't look even slightly believable. If you are going to use a passage of Lorem Ipsum, you need to be sure there isn't anything embarrassing hidden in the middle of text. All the Lorem Ipsum generators on the Internet tend to repeat predefined chunks as necessary, making this the first true generator on the Internet. It uses a dictionary of over 200 Latin words, combined with a handful of model sentence structures, to generate Lorem Ipsum which looks reasonable. The generated Lorem Ipsum is therefore always free from repetition, injected humour, or non-characteristic words etc.</p>
      <p>There are many variations of passages of Lorem Ipsum available, but the majority have suffered alteration in some form, by injected humour, or randomised words which don't look even slightly believable. If you are going to use a passage of Lorem Ipsum, you need to be sure there isn't anything embarrassing hidden in the middle of text. All the Lorem Ipsum generators on the Internet tend to repeat predefined chunks as necessary, making this the first true generator on the Internet. It uses a dictionary of over 200 Latin words, combined with a handful of model sentence structures, to generate Lorem Ipsum which looks reasonable. The generated Lorem Ipsum is therefore always free from repetition, injected humour, or non-characteristic words etc.</p>
    </section>

    <div class="signature" role="img" aria-label="Handwritten signature of the sender"></div>

    <footer class="footer">
      <svg class="footer-band" width="460" height="80" viewBox="0 0 460 80" aria-hidden="true">
        <polygon points="150,56 176,38 452,38 446,56" fill="var(--footer-grey)"/>
        <polygon points="0,52 128,52 168,80 0,80" fill="var(--brand-purple)"/>
      </svg>
      <div class="footer-label label-address">
        <svg viewBox="0 0 8 10"><path d="M4 0a3.2 3.2 0 0 0-3.2 3.2C.8 5.6 4 10 4 10s3.2-4.4 3.2-6.8A3.2 3.2 0 0 0 4 0zm0 4.4a1.2 1.2 0 1 1 0-2.4 1.2 1.2 0 0 1 0 2.4z" fill="#fff"/></svg>
        <span>Lorem ipsum</span>
      </div>
      <div class="footer-label label-phone">
        <svg viewBox="0 0 8 10"><rect x="1.5" y="0.5" width="5" height="9" rx="1" fill="none" stroke="#fff"/><circle cx="4" cy="8" r="0.5" fill="#fff"/></svg>
        <span>Lorem ipsum</span>
      </div>
      <div class="footer-label label-email">
        <svg viewBox="0 0 8 10"><rect x="0.5" y="2.5" width="7" height="5" fill="none" stroke="#fff"/><path d="M0.5 2.5 4 5.5 7.5 2.5" fill="none" stroke="#fff"/></svg>
        <span>Lorem ipsum</span>
      </div>
    </footer>
  </main>
</body>
</html>
```